Popup Banners - BrightCounsel - Legal Technology

- We need two banners (same style) designed with two different images and different text.

- The details of the printing requirements are attached, along with suggested images.

- The banners should share the same theme as our website www.brightcounsel.com.au

- The first banner would include our logo (attached), use the 'roads join' image (attached) in some way and text: New Opportunities - Where legal services and technology meet.

- The second banner would include our logo (attached), use the 'jigsaw' image (attached) in some way and use text: Legal Technology Strategy, Advice and Capability.

- Details on what are required from the Printer is attached also.

Target Market(s)

Legal Professionals

Industry/Entity Type

Information Technology

Font styles to use
Sans Serif

Requirements
Must have
• Our logo (attached), suggested text and the image mentioned for each.
Nice to have
• Professional and modern look
Should not have
• Cheap looking

```html
<!DOCTYPE html>
<html lang="en">
<head>
<meta charset="utf-8">
<title>BrightCounsel – Popup Banners</title>
<link rel="stylesheet" href="https://fonts.googleapis.com/css2?family=Open+Sans:wght@400&family=Arimo:wght@400&display=swap">
<style>
  :root {
    --page-bg: #e4e6e9;
    --band-blue: #5ba3d6;
    --panel-grey: #b9bcc1;
    --ink-blue: #1d5a8a;
    --link-blue: #4b8fc6;
    --white: #ffffff;
    --puzzle-tone-a: #3a5875;
    --puzzle-tone-b: #5b7a98;
    --field-tone: #6f95a2;
  }
  * { margin: 0; padding: 0; box-sizing: border-box; }
  html, body { width: 1200px; height: 973px; overflow: hidden; }
  body {
    background: var(--page-bg);
    position: relative;
    font-family: "Open Sans", sans-serif;
  }
  .banner {
    position: absolute;
    top: 96px;
    width: 342px;
    height: 698px;
    background: var(--panel-grey);
    box-shadow: 0 6px 18px rgba(0,0,0,0.18);
  }
  .banner--strategy { left: 180px; }
  .banner--opportunities { left: 683px; }
  .brand-band {
    height: 81px;
    background: var(--band-blue);
    display: flex;
    align-items: center;
    justify-content: center;
    gap: 12px;
    padding-top: 6px;
  }
  .brand-mark {
    width: 20px; height: 20px;
    background: var(--white);
  }
  .brand-name {
    color: var(--white);
    font-size: 23px;
    font-weight: 400;
    letter-spacing: 4px;
    font-family: "Open Sans", sans-serif;
  }
  .headline {
    position: absolute;
    left: 0; right: 0;
    text-align: center;
    color: var(--ink-blue);
    font-family: "Arimo", sans-serif;
    font-weight: 400;
    font-size: 17.5px;
    line-height: 20px;
    text-transform: uppercase;
  }
  .banner--strategy .headline { top: 118px; }
  .banner--opportunities .headline { top: 106px; }
  .feature-image {
    position: absolute;
    left: 5px;
    width: 333px; height: 333px;
    border-radius: 50%;
  }
  .banner--strategy .feature-image {
    top: 190px;
    background: linear-gradient(160deg, var(--puzzle-tone-b), var(--puzzle-tone-a));
  }
  .banner--opportunities .feature-image {
    top: 192px;
    background: var(--field-tone);
  }
  .call-label {
    position: absolute;
    top: 558px; left: 0; right: 0;
    text-align: center;
    color: var(--ink-blue);
    font-size: 23px;
    font-weight: 400;
  }
  .phone {
    position: absolute;
    top: 583px; left: 0; right: 0;
    text-align: center;
    color: var(--ink-blue);
    font-size: 42px;
    font-weight: 400;
    line-height: 1.2;
  }
  .web {
    position: absolute;
    top: 643px; left: 0; right: 0;
    text-align: center;
    color: var(--link-blue);
    font-size: 14px;
    letter-spacing: 5px;
  }
</style>
</head>
<body>
  <section class="banner banner--strategy">
    <header class="brand-band">
      <span class="brand-mark"></span>
      <span class="brand-name">BrightCounsel</span>
    </header>
    <h2 class="headline">Legal technology strategy,<br>advice and capability.</h2>
    <div class="feature-image" role="img" aria-label="Photo: hand placing a glowing jigsaw puzzle piece"></div>
    <p class="call-label">Call us Now</p>
    <p class="phone">07 3000 0199</p>
    <p class="web">www.brightcounsel.com.au</p>
  </section>

  <section class="banner banner--opportunities">
    <header class="brand-band">
      <span class="brand-mark"></span>
      <span class="brand-name">BrightCounsel</span>
    </header>
    <h2 class="headline">New opportunities<br>where legal services<br>and technology meet</h2>
    <div class="feature-image" role="img" aria-label="Photo: two country roads joining on a grassy hill"></div>
    <p class="call-label">Call us Now</p>
    <p class="phone">07 3000 0199</p>
    <p class="web">www.brightcounsel.com.au</p>
  </section>
</body>
</html>
```